Graphic Design for Beauty Blister Packaging

Seeking visionary designers to create next-level packaging concepts for a dermaplaning tool targeted at North American women aged 18-65. This project combines innovation, elegance, and modern trends, with a particular focus on Y2K-inspired aesthetics blended with minimalist luxury.

See below and attached word document for guidelines and image of product.

What We're Looking For:
We want packaging that not only turns heads but also tells a story of sophistication and self-care. Your design should communicate the following key elements:

Premium Look: Incorporate holographic or foil stamping elements for a high-end, futuristic feel.
Functionality Meets Elegance: Design a clean, user-friendly layout that highlights product benefits and ensures clarity for the customer.
Visual Appeal: Capture a balance between Y2K retro vibes (think holographics, gradients, bold fonts) and modern minimalism (clean lines, simple typography, and elegant spacing).
Brand Integration: Seamlessly incorporate the Movrenta logo and branding elements into your design.
Design Objectives:

Stand out on shelves with a unique, innovative look.
Appeal to a wide demographic by combining timeless beauty with trendy appeal.
Highlight product features such as “Exfoliates,” “Shapes Eyebrows,” and “Removes Fine Hairs” in a way that is both enticing and informative.

Submission Guidelines:

Use holographic gradients and foil stamping as key features of your design.
Include a window to display the product while incorporating chrome-like or holographic borders.
Ensure typography is bold, clean, and aligns with the Y2K theme while being highly legible.
Add a mock-up of how your design would look in retail displays.

Target Market(s)

Women aged 18-65

Industry/Entity Type

Beauty and Cosmetics

Font styles to use
Sans Serif

Requirements
Nice to have
• Y2k theme in a minimalistic style
Should not have
• Cluttered design, excessive icons or designs

```html
<!DOCTYPE html>
<html lang="en">
<head>
<meta charset="utf-8">
<title>Movrenta Dermaplane Razors – Blister Card Options</title>
<link rel="stylesheet" href="https://fonts.googleapis.com/css2?family=Poppins:wght@400;500;600;700;800&display=swap">
<style>
  :root {
    --page: #ffffff;
    --ink: #111111;
    --purple-deep: #5e0f7e;
    --purple: #7a1099;
    --magenta: #ee00e6;
    --plum: #4a0a5c;
    --white: #ffffff;
    --window-line: #e8322f;
    --logo-grey: #4b4b52;
  }
  html, body {
    margin: 0;
    padding: 0;
    width: 1200px;
    height: 870px;
    overflow: hidden;
    background: var(--page);
  }
  .board {
    position: relative;
    width: 1200px;
    height: 870px;
  }
  .board svg { display: block; }
  .option-label {
    font-family: Arial, "Helvetica Neue", sans-serif;
    font-size: 33px;
    fill: var(--ink);
    letter-spacing: 0.5px;
  }
  .product-title {
    font-family: "Poppins", sans-serif;
    font-weight: 800;
    font-size: 33px;
    letter-spacing: -0.6px;
  }
  .product-subtitle {
    font-family: "Poppins", sans-serif;
    font-weight: 400;
    font-size: 23px;
    fill: var(--white);
    letter-spacing: 0.3px;
  }
  .tagline {
    font-family: "Poppins", sans-serif;
    font-weight: 500;
  }
  .tagline--top { font-size: 21px; }
  .tagline--foot { font-size: 13px; }
  .tagline .tone-purple { fill: var(--purple); }
  .tagline .tone-magenta { fill: var(--magenta); }
  .count-text {
    font-family: "Poppins", sans-serif;
    font-weight: 700;
    font-size: 18px;
    fill: #151515;
  }
  .benefit-text {
    font-family: "Poppins", sans-serif;
    font-weight: 500;
    font-size: 9.2px;
    fill: var(--white);
    letter-spacing: 0.2px;
  }
  .side-claim {
    font-family: "Poppins", sans-serif;
    font-weight: 600;
    font-size: 11.6px;
    fill: var(--purple);
    letter-spacing: 0.6px;
  }
  .brand-name {
    font-family: "Poppins", sans-serif;
    font-weight: 400;
    font-size: 30px;
    fill: var(--logo-grey);
  }
</style>
</head>
<body>
<main class="board">
<svg width="1200" height="870" viewBox="0 0 1200 870" xmlns="http://www.w3.org/2000/svg">
  <defs>
    <clipPath id="card-shape">
      <rect x="0" y="0" width="424" height="636" rx="32"/>
    </clipPath>
    <linearGradient id="holo-base" x1="0" y1="0" x2="1" y2="1">
      <stop offset="0" stop-color="#c9d2f0"/>
      <stop offset="0.18" stop-color="#f2bde0"/>
      <stop offset="0.35" stop-color="#bdf2d6"/>
      <stop offset="0.5" stop-color="#c8cdf2"/>
      <stop offset="0.66" stop-color="#e6c2f0"/>
      <stop offset="0.82" stop-color="#b8f0d8"/>
      <stop offset="1" stop-color="#f4b9de"/>
    </linearGradient>
    <linearGradient id="holo-sheen" x1="1" y1="0" x2="0" y2="1">
      <stop offset="0" stop-color="#a6f4cf" stop-opacity="0.6"/>
      <stop offset="0.3" stop-color="#c6cdf0" stop-opacity="0"/>
      <stop offset="0.55" stop-color="#f3b6dc" stop-opacity="0.55"/>
      <stop offset="0.8" stop-color="#c6cdf0" stop-opacity="0"/>
      <stop offset="1" stop-color="#a6f4cf" stop-opacity="0.6"/>
    </linearGradient>
    <linearGradient id="title-fill" x1="0" y1="0" x2="1" y2="0">
      <stop offset="0" stop-color="#5e0f7e"/>
      <stop offset="0.3" stop-color="#b10bb8"/>
      <stop offset="0.5" stop-color="#6e0f8e"/>
      <stop offset="0.72" stop-color="#e800e2"/>
      <stop offset="1" stop-color="#5e0f7e"/>
    </linearGradient>
    <linearGradient id="banner-fill" x1="0" y1="0" x2="1" y2="0">
      <stop offset="0" stop-color="#e35ad8"/>
      <stop offset="0.5" stop-color="#b99cf0"/>
      <stop offset="1" stop-color="#7ff3ee"/>
    </linearGradient>
    <linearGradient id="frame-fill" x1="0" y1="0" x2="0" y2="1">
      <stop offset="0" stop-color="#ffdcc6"/>
      <stop offset="0.3" stop-color="#fbf7c9"/>
      <stop offset="0.65" stop-color="#82efed"/>
      <stop offset="1" stop-color="#e9a0e6"/>
    </linearGradient>
    <linearGradient id="panel-fill" x1="0" y1="0" x2="0" y2="1">
      <stop offset="0" stop-color="#ff00f2"/>
      <stop offset="0.45" stop-color="#c107c7"/>
      <stop offset="1" stop-color="#4a0a5c"/>
    </linearGradient>
    <linearGradient id="chrome" x1="0" y1="0" x2="1" y2="1">
      <stop offset="0" stop-color="#7d7d86"/>
      <stop offset="0.25" stop-color="#f5f5f7"/>
      <stop offset="0.5" stop-color="#9a9aa3"/>
      <stop offset="0.75" stop-color="#ffffff"/>
      <stop offset="1" stop-color="#80808a"/>
    </linearGradient>
    <linearGradient id="pill-fill" x1="0" y1="0" x2="1" y2="0">
      <stop offset="0" stop-color="#ffffff"/>
      <stop offset="0.7" stop-color="#e8e8ec"/>
      <stop offset="1" stop-color="#9e9ea8"/>
    </linearGradient>
    <radialGradient id="seal-fill" cx="0.45" cy="0.4" r="0.7">
      <stop offset="0" stop-color="#f6f0d8"/>
      <stop offset="0.45" stop-color="#a9e6dc"/>
      <stop offset="0.8" stop-color="#b8a9d8"/>
      <stop offset="1" stop-color="#8a8a94"/>
    </radialGradient>
    <linearGradient id="icon-fill" x1="0" y1="0" x2="1" y2="1">
      <stop offset="0" stop-color="#ffffff" stop-opacity="0.55"/>
      <stop offset="1" stop-color="#9ff0ea" stop-opacity="0.35"/>
    </linearGradient>

    <g id="card-base">
      <g clip-path="url(#card-shape)">
        <rect class="card-holo" width="424" height="636" fill="url(#holo-base)"/>
        <rect class="card-sheen" width="424" height="636" fill="url(#holo-sheen)"/>
      </g>

      <path class="hang-hole" d="M170 39 H201 A11 11 0 0 1 223 39 H254 A10 10 0 0 1 264 49 A10 10 0 0 1 254 59 H170 A10 10 0 0 1 160 49 A10 10 0 0 1 170 39 Z" fill="#ffffff" stroke="#222" stroke-width="1.2"/>

      <text class="product-title" x="212" y="94" text-anchor="middle" fill="url(#title-fill)" textLength="359" lengthAdjust="spacingAndGlyphs">DERMAPLANE RAZORS</text>

      <path class="subtitle-band" d="M38 102 H390 V123 Q390 131 382 131 H31 V110 Q31 102 38 102 Z" fill="url(#banner-fill)"/>
      <text class="product-subtitle" x="210" y="125" text-anchor="middle" textLength="342" lengthAdjust="spacingAndGlyphs">FOLDABLE COMPACT RAZORS</text>

      <path class="window-frame" d="M120 562 H82 Q62 562 58 540 L28 190 Q22 140 60 131 M328 131 Q400 135 404 190 Q404 250 392 320 Q386 340 366 350 L364 520 Q362 558 312 562 H304" fill="none" stroke="url(#frame-fill)" stroke-width="8" stroke-linecap="round"/>

      <path class="window-dieline" d="M70 153 H356 Q376 153 376 176 L352 318 Q350 326 342 332 Q337 338 336 350 L330 515 Q329 534 310 534 H103 Q92 534 90 520 L49 180 Q48 153 70 153 Z" fill="none" stroke="var(--window-line)" stroke-width="1"/>

      <path class="benefit-panel" d="M75 330 Q190 355 324 361 L322 526 H108 Z" fill="url(#chrome)"/>
      <path class="benefit-panel-inner" d="M80 337 Q80 333 84 334 Q190 356 316 369 L315 518 H113 Z" fill="url(#panel-fill)"/>
      <path class="panel-band" d="M80 337 Q190 356 316 369 L317 382 Q240 385 150 380 Q110 376 82 368 Z" fill="#ff14f0" opacity="0.6"/>

      <circle class="steel-seal" cx="139" cy="395" r="43" fill="url(#chrome)"/>
      <circle cx="139" cy="395" r="38" fill="url(#seal-fill)" stroke="#1a1a1a" stroke-width="1.5"/>

      <rect class="count-pill" x="208" y="392" width="116" height="23" rx="11.5" fill="url(#pill-fill)"/>
      <text class="count-text" x="262" y="410" text-anchor="middle">9 COUNT</text>

      <rect x="129" y="449" width="36" height="36" rx="8" fill="url(#icon-fill)" role="img" aria-label="Exfoliating brush icon"/>
      <rect x="188" y="449" width="36" height="36" rx="8" fill="url(#icon-fill)" role="img" aria-label="Eyebrow and lash icon"/>
      <rect x="250" y="449" width="36" height="36" rx="8" fill="url(#icon-fill)" role="img" aria-label="Fine hair with sparkles icon"/>

      <text class="benefit-text" x="143" y="501" text-anchor="middle">EXFOLIATES</text>
      <text class="benefit-text" x="206" y="501" text-anchor="middle">SHAPES</text>
      <text class="benefit-text" x="206" y="511" text-anchor="middle">EYEBROW</text>
      <text class="benefit-text" x="268" y="501" text-anchor="middle">REMOVES</text>
      <text class="benefit-text" x="268" y="511" text-anchor="middle">FINE HAIRS</text>

      <text class="side-claim" transform="translate(392 443) rotate(-90)" text-anchor="middle">SIMPLY INNOVATIVE SKIN CARE</text>

      <text class="brand-name" x="224" y="596" text-anchor="middle">Movrenta</text>
    </g>
  </defs>

  <text class="option-label" x="328" y="110" text-anchor="middle">OPTION 1</text>
  <g class="card card--option-1" transform="translate(115 147)">
    <use href="#card-base"/>
    <text class="tagline tagline--top" x="200" y="149" text-anchor="middle"><tspan class="tone-purple">Salon </tspan><tspan class="tone-magenta">Results</tspan><tspan class="tone-purple"> at </tspan><tspan class="tone-magenta">Home</tspan></text>
  </g>

  <text class="option-label" x="873" y="110" text-anchor="middle">OPTION 2</text>
  <g class="card card--option-2" transform="translate(661 147)">
    <use href="#card-base"/>
    <text class="tagline tagline--foot" x="207" y="615"><tspan class="tone-purple">Salon </tspan><tspan class="tone-magenta">Results</tspan><tspan class="tone-purple"> at </tspan><tspan class="tone-magenta">Home</tspan></text>
  </g>
</svg>
</main>
</body>
</html>
```